hi all

Im after a new age looking business card with my company logo on it

must include these details, I would like the PH and Email to be symbols

If the colours used for card could be kept within the colours used in logo that I have supplied that would be great, if another colour is to be used dark grey would be ok. no light bulbs etc thanks

Details below to be incorporated on card

Damian Holloway

Lic E871302

PH 0219647381

E info@brightvaleelectrical.example.nz

Domestic Commercial Industrial Electricians

```html
<!DOCTYPE html>
<html lang="en">
<head>
<meta charset="utf-8">
<title>Brightvale Electrical – Business Card</title>
<link href="https://fonts.googleapis.com/css2?family=Prompt:wght@400;600&display=swap" rel="stylesheet">
<style>
  :root {
    --backdrop: #2a2b2d;
    --brand-blue: #3475bd;
    --brand-navy: #2a5ba6;
    --ink: #1b1b1b;
    --paper: #e7e2de;
    --white: #ffffff;
  }
  * { box-sizing: border-box; margin: 0; padding: 0; }
  html, body {
    width: 1200px; height: 800px; overflow: hidden;
    background: var(--backdrop);
    font-family: "Prompt", sans-serif;
  }
  .canvas {
    position: relative; width: 1200px; height: 800px;
  }
  .card {
    position: absolute; left: 330px; width: 540px; height: 310px;
    overflow: hidden;
  }
  /* Front */
  .card--front { top: 50px; background: var(--brand-blue); }
  .front-brand {
    position: absolute; top: 92px; left: 0; right: 0;
    display: flex; align-items: center; justify-content: center; gap: 14px;
  }
  .brand-dot {
    width: 46px; height: 46px; border-radius: 50%;
    background: var(--ink); flex: none;
  }
  .front-brand .brand-name {
    color: var(--white); font-weight: 600; font-size: 34px;
    letter-spacing: 2px; line-height: 1.05; text-transform: uppercase;
  }
  .brand-name small { display: block; font-size: 15px; letter-spacing: 5px; text-align: right; }
  .tagline-rule {
    position: absolute; left: 0; right: 0; top: 246px;
    display: flex; align-items: center; gap: 8px;
  }
  .tagline-rule::before, .tagline-rule::after {
    content: ""; height: 1.5px; background: var(--white);
  }
  .tagline-rule::before { flex: 0 0 70px; }
  .tagline-rule::after { flex: 1; }
  .tagline { color: var(--white); font-size: 14px; white-space: nowrap; }

  /* Back */
  .card--back { top: 420px; background: var(--paper); }
  .card--back::after {
    content: ""; position: absolute; left: 0; right: 0; bottom: 0; height: 6px;
    background: var(--brand-navy);
  }
  .back-brand {
    position: absolute; left: 30px; top: 110px;
    display: flex; flex-direction: column; align-items: center; gap: 10px;
  }
  .back-brand .brand-dot { width: 50px; height: 50px; }
  .back-brand .brand-name {
    color: var(--brand-navy); font-weight: 600; font-size: 24px;
    letter-spacing: 1.5px; line-height: 1.05; text-transform: uppercase;
  }
  .back-brand .brand-name small { font-size: 11px; letter-spacing: 4px; }
  .contact {
    position: absolute; left: 248px; right: 24px; top: 80px;
  }
  .contact__name {
    color: var(--brand-navy); font-weight: 600; font-size: 20px;
    letter-spacing: 1.5px; text-transform: uppercase; white-space: nowrap;
  }
  .contact__licence { color: var(--ink); font-size: 16px; margin-top: 2px; }
  .contact__list { list-style: none; margin-top: 14px; }
  .contact__item {
    display: flex; align-items: center; gap: 10px;
    color: var(--ink); font-size: 12.5px; margin-bottom: 6px; white-space: nowrap;
  }
  .contact__icon { width: 14px; height: 14px; flex: none; }
</style>
</head>
<body>
<main class="canvas">
  <section class="card card--front" aria-label="Card front">
    <div class="front-brand">
      <span class="brand-dot"></span>
      <p class="brand-name">Brightvale<small>Electrical</small></p>
    </div>
    <div class="tagline-rule">
      <p class="tagline">Domestic Commercial Industrial Electricians</p>
    </div>
  </section>

  <section class="card card--back" aria-label="Card back">
    <div class="back-brand">
      <span class="brand-dot"></span>
      <p class="brand-name">Brightvale<small>Electrical</small></p>
    </div>
    <div class="contact">
      <h1 class="contact__name">Damian Holloway</h1>
      <p class="contact__licence">Lic E871302</p>
      <ul class="contact__list">
        <li class="contact__item">
          <svg class="contact__icon" viewBox="0 0 24 24" fill="none" stroke="#2a5ba6" stroke-width="1.8" stroke-linejoin="round" aria-label="Phone">
            <path d="M5 3h4l2 5-2.5 1.5a11 11 0 0 0 6 6L16 13l5 2v4a2 2 0 0 1-2 2A16 16 0 0 1 3 5a2 2 0 0 1 2-2z"/>
          </svg>
          0219647381
        </li>
        <li class="contact__item">
          <svg class="contact__icon" viewBox="0 0 24 24" fill="none" stroke="#2a5ba6" stroke-width="1.8" stroke-linejoin="round" aria-label="Email">
            <rect x="2" y="5" width="20" height="14"/>
            <path d="M2 5l10 8 10-8M2 19l7-6M22 19l-7-6"/>
          </svg>
          info@brightvaleelectrical.example.nz
        </li>
      </ul>
    </div>
  </section>
</main>
</body>
</html>
```